Verel Institute for Advisory and Learning Prospectus

Design 2 booklets to promote and market my trainings. Please see the attached files. Content attached. Logo is in myy account in Lumo Forge. Please let me know if you cannot access it. I ahve attached a PDF file of a catalouge that is close to what I want. But I want to design mine in smaller size. I also attached the color scheme.

Target Market(s)

parents, educators, students and leaders

Industry/Entity Type

Coaching, Education, Personality Types, Perosnal Development.

Colors
0054AA
0677BA
7BADD7
CADEEF
E8F1F8
00AB8E
00BBA5
67D7C9
C6EFE9
E9F9F6
F0912C
F2A743
F7CA91
FBE8D2
FDF5EE

```html
<!DOCTYPE html>
<html lang="en">
<head>
<meta charset="utf-8">
<title>Verel Institute for Advisory and Learning – Workshops and Trainings Catalogue</title>
<link href="https://fonts.googleapis.com/css2?family=Poppins:wght@300;400;600;700&family=Open+Sans:wght@400;600;700&display=swap" rel="stylesheet">
<style>
  :root{
    --blue-deep:#0054AA;
    --blue:#0677BA;
    --blue-soft:#7BADD7;
    --blue-pale:#E8F1F8;
    --orange:#F0912C;
    --orange-mid:#F2A743;
    --orange-pale:#FBE8D2;
    --navy:#2b323d;
    --ink:#3a3f47;
    --muted:#6b7079;
    --stage:#ececec;
    --white:#ffffff;
  }
  *{box-sizing:border-box;margin:0;padding:0}
  html,body{width:1200px;height:2666px;overflow:hidden}
  body{background:var(--stage);position:relative;font-family:"Open Sans",Arial,sans-serif;color:var(--ink)}

  .page{position:absolute;width:430px;height:600px;background:var(--white);overflow:hidden;box-shadow:0 2px 10px rgba(0,0,0,.12)}
  .heading{font-family:"Poppins",Arial,sans-serif}

  .page-rule{position:absolute;left:0;right:0;bottom:0;height:10px}
  .page-rule::before{content:"";position:absolute;left:0;right:0;top:0;height:3px;background:var(--orange)}
  .page-rule::after{content:"";position:absolute;left:0;right:0;bottom:0;height:5px;background:var(--navy)}

  /* ---------- cover ---------- */
  .brand{position:absolute;left:0;right:0;top:20px;display:flex;justify-content:center;align-items:center;gap:7px;font-family:"Poppins",Arial,sans-serif;font-weight:700;font-size:24px;color:var(--blue-deep);letter-spacing:1px}
  .brand-dot{width:14px;height:14px;border-radius:50%;background:var(--orange)}
  .cover-strip{position:absolute;left:0;right:0;top:66px;height:22px;background:var(--navy);color:var(--white);font-family:"Poppins",Arial,sans-serif;font-size:8.5px;font-weight:600;line-height:22px;padding-left:40px}
  .cover-photo{position:absolute;left:0;right:0;top:88px;height:222px;background:linear-gradient(135deg,#6d6a66 0%,#9a948c 35%,#5a5550 60%,#bfb6a8 100%)}
  .cover-motto{position:absolute;left:0;right:0;top:290px;height:98px;background:var(--blue);clip-path:polygon(0 22%,100% 0,100% 100%,0 100%);display:flex;align-items:center;justify-content:center;padding:18px 40px 0;text-align:center;color:var(--white);font-family:"Poppins",Arial,sans-serif;font-weight:700;font-size:15px;line-height:1.3}
  .cover-title{position:absolute;right:24px;top:432px;font-family:"Poppins",Arial,sans-serif;font-size:10.5px;font-weight:600;color:var(--navy)}
  .cover-title-rule{position:absolute;left:0;right:0;top:452px;height:2px;background:var(--orange)}
  .cover-seal{position:absolute;left:40px;top:478px;width:46px;height:46px;border-radius:50%;background:radial-gradient(circle,#f3cf63 0%,#c9962c 75%);border:3px solid #e3b64a}
  .cover-base{position:absolute;left:0;right:0;bottom:0;height:14px;background:linear-gradient(to bottom,var(--blue-pale) 0,var(--blue-pale) 50%,var(--orange) 50%)}

  /* ---------- back cover ---------- */
  .back{background:linear-gradient(150deg,var(--orange-mid) 0%,var(--orange) 100%);color:var(--white);text-align:center}
  .back-brand{position:absolute;left:0;right:0;top:230px;display:flex;justify-content:center;align-items:center;gap:10px;font-family:"Poppins",Arial,sans-serif;font-weight:700;font-size:44px;letter-spacing:2px}
  .back-brand-mark{width:22px;height:22px;border:3px solid var(--white)}
  .back-contact{position:absolute;left:0;right:0;top:330px;font-family:"Poppins",Arial,sans-serif}
  .back-contact .label{font-size:11px;font-weight:400;letter-spacing:.5px}
  .back-contact .sub{font-size:10px;font-weight:300;margin-top:4px}
  .back-contact .value{font-size:13px;font-weight:700;margin-top:3px}
  .back-contact .gap{margin-top:18px}

  /* ---------- spread one ---------- */
  .intro-photo{position:absolute;left:0;right:0;top:0;height:250px;background:linear-gradient(120deg,#b8b0a4 0%,#8b8179 40%,#d6cfc6 70%,#a49a8f 100%)}
  .about-panel{position:absolute;left:0;top:250px;width:245px;height:350px;background:var(--blue);border-top:7px solid var(--navy);border-right:7px solid var(--navy);border-top-right-radius:48px;padding:26px 18px 0 20px;color:var(--white)}
  .about-panel h3{font-family:"Poppins",Arial,sans-serif;font-size:11px;font-weight:700;line-height:1.2;margin-bottom:6px}
  .about-panel p{font-size:7.2px;line-height:1.45;margin-bottom:14px}
  .statement{position:absolute;left:262px;width:155px;text-align:center}
  .statement h4{font-family:"Poppins",Arial,sans-serif;font-weight:300;font-size:19px;color:var(--blue);letter-spacing:.5px}
  .statement h4 .quote{color:var(--navy);font-weight:700;font-size:20px;margin-right:2px}
  .statement p{font-size:8px;line-height:1.4;color:var(--muted);margin-top:4px}
  .statement p .quote{color:var(--navy);font-weight:700;font-size:12px}
  .mini-contact{position:absolute;left:262px;top:520px;width:160px;text-align:center;font-size:7px;line-height:1.5;color:var(--ink)}
  .mini-contact strong{display:block;font-size:7.5px}

  .founder-title{position:absolute;left:28px;top:30px;font-family:"Poppins",Arial,sans-serif;font-weight:700;font-size:15px;color:var(--blue)}
  .founder-title span{color:var(--orange)}
  .founder-portrait{position:absolute;right:26px;top:18px;width:64px;height:70px;background:linear-gradient(160deg,#e8e5e0 0%,#b9aea2 60%,#6e655d 100%);border:2px solid var(--white);box-shadow:0 1px 4px rgba(0,0,0,.2)}
  .founder-text{position:absolute;left:28px;top:56px;width:374px;font-size:7.3px;line-height:1.5;color:var(--ink);text-align:justify}
  .founder-text p{margin-bottom:8px}
  .founder-text p:first-child{width:290px}
  .founder-text strong{color:var(--orange)}
  .founder-fade{position:absolute;left:0;right:0;top:380px;height:210px;background:linear-gradient(to bottom,#ffffff 0%,rgba(205,200,194,.55) 35%,rgba(190,185,178,.45) 100%)}

  /* ---------- spread two ---------- */
  .services-photo{position:absolute;inset:0;background:linear-gradient(140deg,#4d4a48 0%,#6b645e 35%,#3f3c3b 70%,#57524e 100%)}
  .consult-card{position:absolute;left:212px;top:250px;width:200px;height:310px;background:var(--white);border-radius:26px 26px 26px 0;padding:20px 16px 0 18px}
  .consult-card h5{font-family:"Poppins",Arial,sans-serif;font-size:9.5px;font-weight:700;color:var(--orange);margin-bottom:4px}
  .consult-card p{font-size:7.2px;line-height:1.45;color:var(--ink);margin-bottom:8px}
  .consult-photo{position:absolute;left:14px;right:14px;bottom:14px;height:112px;border-radius:10px;background:linear-gradient(130deg,#a59a86 0%,#6f6a60 50%,#c0b49d 100%)}
  .service-box{position:absolute;left:62px;width:200px;padding:16px 14px 0 16px;color:var(--white)}
  .service-box h5{font-family:"Poppins",Arial,sans-serif;font-size:11px;font-weight:700;margin-bottom:3px}
  .service-box p{font-size:7.2px;line-height:1.45}
  .service-training{top:372px;height:120px;background:var(--orange);border-top-left-radius:26px}
  .service-coaching{top:492px;height:108px;background:var(--blue)}

  .pdf-title{position:absolute;left:28px;top:24px;width:380px;font-family:"Poppins",Arial,sans-serif;font-weight:700;font-size:13px;line-height:1.25;color:var(--blue)}
  .pdf-title span{color:var(--orange)}
  .pdf-intro{position:absolute;left:28px;top:62px;width:380px;font-size:7.2px;line-height:1.5;text-align:justify}
  .pdf-list{position:absolute;left:28px;top:146px;width:380px;list-style:none;font-size:7.2px;line-height:1.4}
  .pdf-list li{margin-bottom:5px}
  .pdf-list li.narrow{width:220px}
  .pdf-list b{font-weight:700;color:var(--navy)}
  .pdf-photo{position:absolute;right:0;top:318px;width:170px;height:250px;background:linear-gradient(150deg,#ddd8d0 0%,#9c948a 55%,#3c3a3a 100%);border:7px solid var(--navy);border-right:none;border-radius:46px 0 0 46px}
</style>
</head>
<body>

<section class="page cover" style="left:385px;top:53px">
  <div class="brand"><span class="brand-dot"></span>VIAL</div>
  <div class="cover-strip">VIAL Personality Types Workshops and Coaching</div>
  <div class="cover-photo" role="img" aria-label="Photo of the facilitator presenting to a seated workshop group"></div>
  <div class="cover-motto">Motto Discover Your True Personality Type and Bring Wellness to Your Personal and Professional Life</div>
  <div class="cover-title">Workshops and Trainings Catalogue</div>
  <div class="cover-title-rule"></div>
  <div class="cover-seal" role="img" aria-label="Certified facilitator seal"></div>
  <div class="cover-base"></div>
</section>

<section class="page back" style="left:170px;top:706px">
  <div class="back-brand"><span class="back-brand-mark"></span>VIAL</div>
  <div class="back-contact">
    <div class="label">CONTACT US</div>
    <div class="sub">Contact:</div>
    <div class="value">(idris.hallam@mailbox.org)</div>
    <div class="sub gap">Phone:</div>
    <div class="value">313.555.0147/ 801-555-0193</div>
  </div>
</section>
<section class="page cover" style="left:600px;top:706px">
  <div class="brand"><span class="brand-dot"></span>VIAL</div>
  <div class="cover-strip">VIAL Personality Types Workshops and Coaching</div>
  <div class="cover-photo" role="img" aria-label="Photo of the facilitator presenting to a seated workshop group"></div>
  <div class="cover-motto">Motto Discover Your True Personality Type and Bring Wellness to Your Personal and Professional Life</div>
  <div class="cover-title">Workshops and Trainings Catalogue</div>
  <div class="cover-title-rule"></div>
  <div class="cover-seal" role="img" aria-label="Certified facilitator seal"></div>
  <div class="cover-base"></div>
</section>

<section class="page" style="left:170px;top:1359px">
  <div class="intro-photo" role="img" aria-label="Photo of a workshop session with participants seated at tables"></div>
  <div class="about-panel">
    <h3>About Verel Institute for Advisory and Learning</h3>
    <p>VIAL's mission is to empower personal and professional change through self-awareness. We believe that self-awareness instills confidence and holistic well-being. Our training, coaching, and consulting services empower our trainees with the professional and soft skills necessary to achieve success.</p>
    <h3>VIAL APPROACH</h3>
    <p>VIAL services utilize active learning strategies to create an open environment for trainees to discuss and practice communication, critical and creative thinking, collaboration and team building through practical applications. We offer specialty services in: a) Personality Development &amp; Fitness (PDF) and b) Islamic School Education. See below for more information on the training offerings.</p>
  </div>
  <div class="statement" style="top:268px">
    <h4><span class="quote">“</span>MISSION</h4>
    <p>Promoting well-being and mindfulness through training, advocacy, and community engagement. <span class="quote">”</span></p>
  </div>
  <div class="statement" style="top:384px">
    <h4><span class="quote">“</span>VISION</h4>
    <p>Informed, empowered, mindful, empathetic and successful communities shaped by people of all capabilities. <span class="quote">”</span></p>
  </div>
  <div class="mini-contact">
    <strong>CONTACT US</strong>
    Contact: (idris.hallam@mailbox.org)<br>
    Phone: 313.555.0147/ 801-555-0193
  </div>
  <div class="page-rule"></div>
</section>
<section class="page" style="left:600px;top:1359px">
  <h2 class="founder-title heading">ABOUT THE <span>FOUNDER</span></h2>
  <div class="founder-portrait" role="img" aria-label="Portrait photo of the founder"></div>
  <div class="founder-text">
    <p>Idris Hallam holds a PhD in Arabic and linguistics from the Westbrook University and has taught and lectured at several universities in both the US and the Middle East. He is currently the director of the Arabic Language Institute at the Lakeside Islamic College in Chicago and serves as an educational consultant in curriculum and teaching methodology.</p>
    <p>Additionally, Dr. Hallam is a certified facilitator in personality types, an active community member, a public speaker, and a certified instructor in Community Wellness Response (CWR) by the National Wellness Council. <strong>DR. HALLAM</strong> is the founder of <strong>VEREL INSTITUTE FOR ADVISORY AND LEARNING (VIAL) LLC.</strong> (www.verelinstitute.org (coming soon)) where he hosts personal and professional development workshops.</p>
    <p>“My passion is to coach, train and facilitate workshops, domestically and abroad. Anyone who knows me can attest that I really know and love what I am doing. I enjoy helping people from all walks of life, ages and backgrounds to discover their unique personality types and traits, improve communication and recognize their true selves.</p>
    <p>I both design and facilitate customized workshops, known for their engaging presentation style, rich content, and for meeting objectives. I meet both individual and institutional needs. Sponsoring organizations are consistently satisfied with their return on investment (ROI).”</p>
  </div>
  <div class="founder-fade" role="img" aria-label="Faded photo of a workshop room"></div>
  <div class="page-rule"></div>
</section>

<section class="page" style="left:170px;top:2012px">
  <div class="services-photo" role="img" aria-label="Dark-toned photo of workshop participants"></div>
  <div class="consult-card">
    <h5>CONSULTING</h5>
    <p>Comprehensive consulting, training, and coaching services to improve instruction in Islamic schools.</p>
    <p>We offer custom programs that aim to develop teachers' competencies through observation, training workshops, and follow-up coaching.</p>
    <div class="consult-photo" role="img" aria-label="Photo of a classroom group"></div>
  </div>
  <div class="service-box service-training">
    <h5>TRAINING</h5>
    <p>Workshops for individuals, institutional and community groups on personality types, curriculum and instruction development in Arabic, Islamic Studies and Quran, and Social Emotional Learning.</p>
  </div>
  <div class="service-box service-coaching">
    <h5>COACHING</h5>
    <p>Hourly sessions offered to individuals, partners, families, or small groups centered on self-awareness, personality type fitness, and personal development.</p>
  </div>
  <div class="page-rule"></div>
</section>
<section class="page" style="left:600px;top:2012px">
  <h2 class="pdf-title">PERSONALITY DEVELOPMENT <span>&amp; FITNESS (PDF)</span><br><span>WORKSHOPS</span></h2>
  <p class="pdf-intro">Personality Development &amp; Fitness (PDF) training is research-based and proven to help people discover and utilize their authentic personality type to build resilience, excel in their personal life, and achieve professional goals. Through VIAL workshops, participants have a better understanding of one's own tendencies and the tendencies of others in order to reach our fullest potential. Participants will gain better understanding of their values, joys, stressors and communication styles. The following PDF workshops are designed to improve communication, leadership, and problem-solving skills –</p>
  <ul class="pdf-list">
    <li><b>PDF0100 Personality Types and Success –</b> For: grades 5-12</li>
    <li><b>PDF0101 Personality Types and Success</b> (For: Everyone)</li>
    <li><b>PDF0102 Personality Types in the Classroom</b> (For: Educators, School Administrators) <b>PDF0103 Personality Types For Couples</b> (For: Spouses; Couples-to-be; Religious organizations; Family and marriage counselors)</li>
    <li class="narrow"><b>PDF0104 Personality Types For Parents</b> (For: Parents; Educators)</li>
    <li class="narrow"><b>PDF0105 Personality Types For Major and Career</b> (For: Students; Educators; Parents; Counsellors)</li>
    <li class="narrow"><b>PDF0106 Personality Types and Leadership</b> (For: Managers; Directors; Leaders; Board members; Parents)</li>
    <li class="narrow"><b>PDF0107 Personality Types and Health Care</b> (For: Physicians; Nurses; Health System staff)</li>
    <li class="narrow"><b>PDF0108 Personality Types and Conflict Resolution</b> (For: Leaders; Mediators; Educators; Parents; Managers; HR)</li>
    <li class="narrow"><b>PDF0109 Personality Types and Business</b> (For: Business Owners; Salespersons; Product-Owners)</li>
    <li class="narrow"><b>PT0100 PT0101 PT0102 PT0103 PT0104 PT0105 PT0106 PT0107 PT0108 PT0109</b></li>
  </ul>
  <div class="pdf-photo" role="img" aria-label="Photo of the facilitator speaking to an audience"></div>
  <div class="page-rule"></div>
</section>

</body>
</html>
```